Website design for an Italian restaurant in Amsterdam

I need a design for a client of mine. It is for Teatro Lunaverde, an Italian restaurant in Amsterdam.
We are going for a clean, modern look but we also need to realise an authentic feel.
The restaurant is located in an old movie theatre, that is where the name Teatro Lunaverde comes from.
Industry/Entity Type
Italian Restaurant
Number of Pages Required
1 page
Font styles to use
Sans Serif
Colors
Designer to choose colors to be used in the design.

```html
<!DOCTYPE html>
<html lang="en">
<head>
<meta charset="utf-8">
<title>Teatro Lunaverde – Ristorante Italiano</title>
<link rel="stylesheet" href="https://fonts.googleapis.com/css2?family=Bodoni+Moda:ital,wght@0,500;1,500;1,600&family=Montserrat:wght@500;600;700&display=swap">
<style>
  :root {
    --rose: #b04a5a;
    --ink: #1c1c1e;
    --paper: #ffffff;
    --hero-dark: #1b1d20;
    --hero-mid: #3a3d40;
    --hero-warm: #5b4a3a;
    --muted: #6d6d70;
  }
  * { box-sizing: border-box; margin: 0; padding: 0; }
  html, body {
    width: 1200px; height: 900px; overflow: hidden;
    background: var(--paper);
    font-family: "Montserrat", sans-serif;
    color: var(--ink);
  }
  .page { position: relative; width: 1200px; height: 900px; overflow: hidden; }

  .site-header { position: relative; height: 140px; }
  .call-button, .reservation-button {
    position: absolute; top: 34px;
    border: 1.5px solid var(--rose); color: var(--rose);
    font-size: 10px; font-weight: 600; letter-spacing: 1.5px;
    text-transform: uppercase; padding: 7px 16px;
  }
  .call-button { left: 60px; }
  .reservation-button { right: 60px; padding: 7px 40px; }

  .brand {
    position: absolute; left: 50%; top: 30px; transform: translateX(-50%);
    text-align: center;
  }
  .brand-mark {
    display: block; width: 10px; height: 10px; margin: 0 auto 8px;
    border-radius: 50%; background: var(--rose);
  }
  .brand-name {
    font-family: "Bodoni Moda", serif; font-weight: 500;
    font-size: 24px; letter-spacing: 0.5px; text-transform: uppercase;
    color: var(--ink); white-space: nowrap;
  }
  .brand-tagline {
    font-size: 12px; font-weight: 500; color: var(--rose);
    letter-spacing: 1px; margin-top: 2px;
  }

  .main-nav { position: absolute; top: 96px; left: 60px; right: 60px; }
  .nav-group { position: absolute; top: 0; display: flex; gap: 56px; }
  .nav-group.left { left: 0; }
  .nav-group.right { right: 0; }
  .nav-link {
    font-size: 10px; font-weight: 700; letter-spacing: 1.5px;
    text-transform: uppercase; color: var(--ink);
  }
  .nav-link.is-active { color: var(--rose); border-bottom: 1.5px solid var(--rose); padding-bottom: 3px; }

  .hero {
    position: absolute; top: 150px; left: 40px; right: 40px; height: 540px;
  }
  .hero-photo {
    position: absolute; inset: 0;
    background:
      radial-gradient(ellipse at 50% 20%, rgba(120,110,95,0.55), transparent 55%),
      linear-gradient(180deg, var(--hero-dark) 0%, var(--hero-mid) 55%, var(--hero-warm) 100%);
  }
  .hero-content {
    position: absolute; inset: 0; display: flex; flex-direction: column;
    align-items: center; justify-content: center; color: var(--paper);
  }
  .hero-address {
    font-family: "Bodoni Moda", serif; font-style: italic; font-weight: 500;
    font-size: 22px; margin-bottom: 4px;
  }
  .hero-title {
    font-family: "Bodoni Moda", serif; font-style: italic; font-weight: 600;
    font-size: 64px; letter-spacing: 1px; text-transform: uppercase;
  }
  .hero-button {
    margin-top: 26px; background: var(--paper); color: var(--rose);
    font-size: 10px; font-weight: 700; letter-spacing: 1.5px;
    padding: 11px 30px; text-transform: uppercase;
  }
  .hero-scroll { position: absolute; bottom: 22px; left: 50%; transform: translateX(-50%); }

  .about { position: absolute; top: 730px; left: 60px; right: 60px; height: 200px; }
  .about-title {
    font-family: "Bodoni Moda", serif; font-style: italic; font-weight: 500;
    font-size: 26px;
  }
  .about-title .accent { color: var(--rose); }
  .about-text { margin-top: 14px; width: 460px; font-size: 13px; line-height: 1.7; color: var(--muted); }
  .about-photo {
    position: absolute; top: 0; right: 120px; width: 360px; height: 200px;
    background: linear-gradient(160deg, #2c3550 0%, #5a4a63 50%, #b0707a 100%);
  }
</style>
</head>
<body>
<div class="page">
  <header class="site-header">
    <div class="call-button">Call: (+31) 20 555 0147</div>
    <div class="brand">
      <span class="brand-mark"></span>
      <div class="brand-name">Teatro Lunaverde</div>
      <div class="brand-tagline">Ristorante Italiano</div>
    </div>
    <div class="reservation-button">Reservation</div>
    <nav class="main-nav">
      <div class="nav-group left">
        <span class="nav-link is-active">Home</span>
        <span class="nav-link">About</span>
        <span class="nav-link">Menu (New)</span>
      </div>
      <div class="nav-group right">
        <span class="nav-link">Group Menu</span>
        <span class="nav-link">Gallery</span>
        <span class="nav-link">Contact</span>
      </div>
    </nav>
  </header>

  <section class="hero">
    <div class="hero-photo" role="img" aria-label="Dimly lit modern restaurant interior with round ceiling lights, white chairs and plants"></div>
    <div class="hero-content">
      <div class="hero-address">Keizerlaan 42</div>
      <h1 class="hero-title">In the City Center</h1>
      <div class="hero-button">Contact Us</div>
    </div>
    <svg class="hero-scroll" width="14" height="10" viewBox="0 0 14 10" aria-hidden="true">
      <path d="M2 2 L7 7 L12 2" fill="none" stroke="#ffffff" stroke-width="1.6"/>
    </svg>
  </section>

  <section class="about">
    <h2 class="about-title">About the <span class="accent">Teatro Lunaverde</span></h2>
    <p class="about-text">Italian cooking served in the halls of an old movie theatre, right in the heart of Amsterdam.</p>
    <div class="about-photo" role="img" aria-label="Evening view of the restaurant's theatre facade"></div>
  </section>
</div>
</body>
</html>
```